B2B modern industry lubrication label

We are a chemical company that needs a new, very modern outstanding lubrication packaging label. The logo attached can be changed in color. The name of the product is R83. Attached also the text you can use, please disregard the current layout of the text, you can make it any layout you want. Be free in font type, colors and other design aspects.
Dimensions: 21 x 14,8 cm
industry, companies with machinery
Industrial

```html
<!DOCTYPE html>
<html lang="en">
<head>
<meta charset="utf-8">
<title>HALVERN R83 PRO – Lubrication Label</title>
<link rel="stylesheet" href="https://fonts.googleapis.com/css2?family=Montserrat:wght@500;700;800;900&display=swap">
<style>
  :root {
    --bg: #e6e6e8;
    --gold-light: #f6d24a;
    --gold: #e2a816;
    --gold-deep: #b86d0c;
    --amber-dark: #7a3d08;
    --band: #0d0d0d;
    --white: #f4f4f4;
    --ink: #3a2a08;
    --brand-fill: #efe6b0;
  }
  * { margin: 0; padding: 0; box-sizing: border-box; }
  html, body {
    width: 1200px; height: 1200px; overflow: hidden;
    background: var(--bg);
    font-family: "Montserrat", Arial, sans-serif;
  }
  .canvas {
    position: relative; width: 1200px; height: 1200px;
    display: flex; align-items: center; justify-content: center;
  }
  .label {
    position: relative; width: 440px; height: 1000px; overflow: hidden;
    box-shadow: 0 18px 40px rgba(0,0,0,0.18);
  }
  .label-artwork {
    position: absolute; inset: 0;
    background:
      radial-gradient(ellipse at 30% 20%, var(--gold-deep) 0%, transparent 55%),
      radial-gradient(ellipse at 70% 75%, var(--gold-light) 0%, transparent 50%),
      linear-gradient(160deg, var(--gold) 0%, var(--gold-deep) 35%, var(--amber-dark) 50%, var(--gold) 65%, var(--gold-light) 100%);
  }
  .brand {
    position: absolute; top: 70px; left: 0; right: 0;
    text-align: center;
    font-weight: 900; font-size: 50px; letter-spacing: 0.5px;
    color: var(--brand-fill);
  }
  .product-band {
    position: absolute; left: -160px; top: 400px;
    width: 760px; height: 240px;
    transform: rotate(-22deg);
    background: var(--band);
    border-top: 3px solid var(--gold);
    border-bottom: 3px solid var(--gold);
    display: flex; flex-direction: column; align-items: center; justify-content: center;
    color: var(--white);
  }
  .band-claim {
    font-weight: 700; font-size: 17px; letter-spacing: 0.5px; text-transform: uppercase;
  }
  .product-name {
    display: flex; align-items: flex-end; line-height: 1; margin: 6px 0 10px;
  }
  .product-code { font-weight: 800; font-size: 118px; letter-spacing: -4px; }
  .product-tier { font-weight: 800; font-size: 34px; margin: 0 0 14px 6px; }
  .specs {
    position: absolute; bottom: 60px; left: 0; right: 0;
    text-align: center; color: var(--ink);
  }
  .spec-colour { font-weight: 500; font-size: 19px; letter-spacing: 1px; margin-bottom: 14px; }
  .spec-line { font-weight: 500; font-size: 13px; letter-spacing: 1px; line-height: 1.5; }
</style>
</head>
<body>
<main class="canvas">
  <section class="label">
    <div class="label-artwork" role="img" aria-label="Abstract golden swirling ribbons background"></div>
    <div class="brand">HALVERN</div>
    <div class="product-band">
      <p class="band-claim">For a durable lubrication</p>
      <h1 class="product-name"><span class="product-code">R83</span><span class="product-tier">PRO</span></h1>
      <p class="band-claim">With extreme pressure</p>
    </div>
    <div class="specs">
      <p class="spec-colour">YELLOW</p>
      <p class="spec-line">1.07 G/ML</p>
      <p class="spec-line">-40 UNTIL 370 °C</p>
    </div>
  </section>
</main>
</body>
</html>
```